Exciting, Bold and Modern Landscaping & Turf care company business card

Hello, I own a lawn and landscaping company in Virginia, USA. We would like to design a bold, dynamic, modern business card that really makes us stand out. I tire of all green business cards with crappy, cartoonish clipart grass on them. It needs to be two sided, on one side i need to highlight our turf care division called "Promised Brighter Meadow" We maintain grass, fertilize it, weed control, etc.. We have a green thumbed gopher as our logo that i will attach. I am looking for something, clean and neat but out of the box in style. Im open to all ideas, and would like different options for them. On the other side, i want to highlight our landscaping division "Quiet Harbor Landscaping" In this division we design and install landscapes. Feel free to visit our website for more info or email me with ANY questions. Our busines cards in the past have highlighted our different services, but i don't want to this time. By the time I hand out a business card we are usually already estimating a project and they know what services we offer. I do want them to look at my card and say "wow thats pretty cool" and for them to think "These guys are something different, not just your standard dirt diggers" The logo doesnt have to be on both sides, but it needs to be on the turf care side. Our phone number and website should also be on at least on side, but need not be on both. The phone number is (555)618-4072 as well as the web address as www.MossbrookYardWorks.example. I like for the web address to have caps like that becasue it makes the long address much easier to read. I would like it in full color, printing costs are not my major concern. I also love rounded corners or interesting die cut designs as well, so feel free to wow me. Whether it be a clean white background with a bold photo to an all black card with a gray logo except for his green thumb with silver foil lettering to anything in between, lets go for it. That bieng said i dont want anything cartoonish, we are still a professional service and i want that to come through. THANKS!
Updates
Project Deadline Extended
Reason: changed project to a committed payment. I would like designers to re-evaluate their interest now and give them extra time to submit designs. Thank you.
we have changed our status to a commited payment to entice more submissions. thank you all for your hard work!
Industry/Entity Type
Professional Service
Look and feel
Each slider illustrates characteristics of the customer's brand and the style your logo design should communicate.

```html
<!DOCTYPE html>
<html lang="en">
<head>
<meta charset="utf-8">
<title>Quiet Harbor Landscaping – Business Cards</title>
<link rel="stylesheet" href="https://fonts.googleapis.com/css2?family=Yanone+Kaffeesatz:wght@400;600;700&display=swap">
<style>
  :root {
    --stage: #8b8c8e;
    --ink: #000000;
    --paper: #ffffff;
    --leaf: #8dc63f;
    --sun: #f2d21b;
    --stripe-a: #3f8f2c;
    --stripe-b: #6cbf3a;
    --garden-top: #3d6b2a;
    --garden-mid: #6f9a3a;
    --garden-low: #8f8a86;
    --lawn-sky: #cfe3f2;
    --lawn-green: #4f8f2e;
  }
  * { margin: 0; padding: 0; box-sizing: border-box; }
  html, body { width: 1200px; height: 933px; overflow: hidden; background: var(--stage); }
  body { position: relative; font-family: "Yanone Kaffeesatz", "Arial Narrow", sans-serif; }

  .card {
    position: absolute;
    width: 574px;
    height: 343px;
    border-radius: 22px;
    overflow: hidden;
    background: var(--ink);
  }
  .card svg.art { position: absolute; inset: 0; width: 100%; height: 100%; }

  /* Landscaping side */
  .card--landscaping { left: 135px; top: 94px; }
  .garden-photo {
    position: absolute; inset: 0;
    background: linear-gradient(180deg, var(--garden-top) 0%, var(--garden-mid) 32%, #4b6e2c 62%, var(--garden-low) 82%, #7b5a3a 100%);
  }
  .company-name {
    position: absolute; left: 0; right: 0; top: 142px;
    text-align: center; font-weight: 600; font-size: 42px; letter-spacing: 0.5px;
    color: var(--leaf); line-height: 1;
  }

  /* Turf care side */
  .card--turf { left: 475px; top: 487px; }
  .lawn-scene {
    position: absolute; left: 0; top: 0; width: 220px; height: 100%;
    background: linear-gradient(180deg, var(--lawn-sky) 0%, #a9cbe3 22%, #3e7a2a 38%, var(--lawn-green) 70%, #6aa83e 100%);
  }
  .company-mark {
    position: absolute; left: 14px; width: 176px; top: 140px;
    text-align: center; font-weight: 600; font-size: 28px; line-height: 1.05;
    color: var(--paper);
  }
  .turf-text {
    position: absolute; left: 220px; right: 0; top: 0; bottom: 0;
    color: var(--leaf); text-align: center;
  }
  .website { position: absolute; left: 0; right: 0; top: 24px; font-size: 21px; font-weight: 400; }
  .slogan {
    position: absolute; left: 12px; right: 0; top: 95px;
    font-size: 35px; font-weight: 700; text-align: left; letter-spacing: 0.3px;
  }
  .slogan .accent { color: var(--sun); }
  .grass-stripe {
    position: absolute; left: 0; right: 0; top: 140px; height: 16px;
    background: repeating-linear-gradient(90deg, var(--stripe-a) 0 40px, var(--stripe-b) 40px 80px);
  }
  .name { position: absolute; left: 0; right: 0; top: 218px; font-size: 33px; font-weight: 600; letter-spacing: 0.5px; }
  .phone { position: absolute; left: 0; right: 0; top: 262px; font-size: 25px; font-weight: 400; }
  .email { position: absolute; left: 0; right: 0; top: 296px; font-size: 17px; font-weight: 400; }
</style>
</head>
<body>

<section class="card card--landscaping" aria-label="Landscaping division side">
  <div class="garden-photo" role="img" aria-label="Photo of a landscaped garden with evergreens, stone steps, boulders and gravel path"></div>
  <svg class="art" viewBox="0 0 574 343" preserveAspectRatio="none" aria-hidden="true">
    <polygon fill="#000"
      points="0,120 30,112 60,118 95,108 130,116 170,106 210,114 250,104 290,112 330,102 370,110 410,100 450,108 490,98 530,106 574,96
              574,214 540,222 500,212 460,224 420,214 380,226 340,216 300,228 260,218 220,230 180,220 140,232 100,222 60,234 30,224 0,232"/>
  </svg>
  <h1 class="company-name">QUIET HARBOR LANDSCAPING</h1>
</section>

<section class="card card--turf" aria-label="Turf care division side">
  <div class="lawn-scene" role="img" aria-label="Lawn and trees under a blue sky where the company mascot stands"></div>
  <p class="company-mark">Quiet Harbor Landscaping</p>
  <svg class="art" viewBox="0 0 574 343" preserveAspectRatio="none" aria-hidden="true">
    <polygon fill="#000"
      points="196,0 204,20 192,42 206,66 194,92 208,118 196,146 210,172 198,200 212,228 200,256 214,284 202,312 212,343 574,343 574,0"/>
  </svg>
  <div class="turf-text">
    <p class="website">www.MossbrookYardWorks.example</p>
    <h2 class="slogan"><span class="accent">PROMISED</span> BRIGHTER MEADOW</h2>
    <div class="grass-stripe"></div>
    <p class="name">DANIEL HARPER</p>
    <p class="phone">P: 555-618-4072</p>
    <p class="email">E: QuietHarborLandscaping@mailbox.example</p>
  </div>
</section>

</body>
</html>
```